依頼詳細
デザイン住宅の看板デザインをお願いします。
生活道路沿いの路上看板のデザインになります。
事務所上の看板デザインに沿って頂き、シンプルで目立つ看板のデザインでお願いします。
記載項目
会社名:株式会社キリノハコビヤ
電話番号:0574-83-5167
ロゴ(添付ファイル)
看板写真(添付ファイル:宮鶴屋さんの下部分になります)
参考:事務所上の看板(添付ファイル)
希望イメージ
希望する色
水色系、無彩色系
納品ファイル
• 高解像度JPG (.jpg)
• イラストレーター形式 (.ai)
• フォトショップ形式 (.psd)
• PNG形式 (.png)
補足説明
〇想い
高性能でカッコいい家をどこよりもお値打ちに
家づくりは楽しくなくてはならない
家族みんなが毎日笑顔になるオリジナルの家
想いをカタチにできる家
地震に強く、高性能は当たり前

〇メインターゲット
子育て世代・共働き世代
大手ハウスメーカー層から降りてこられるお客様
デザイン住宅(設計事務所)から降りてこられるお客様
看板サイズ 幅1350mm×高さ2500mm

看板の位置の写真の追加させて頂きます。
■ 選んだ理由

シンプルさの中に、親しみを一番感じました。
優しいコントラストの中に、温かみも含まれてると感じ、
こちらのご提案を採用させて頂きました。

■ 提案者全員のお礼・コメント

たくさんのご提案を頂き、ありがとうございました!
正直こんなにご提案頂けるとは思っておらず、
皆さまのデザインに対する想いがすごく伝わり、とても勉強になりました。
次の機会があれば、またご依頼させて頂きたいと思います。
ありがとうございました!

```html
<!DOCTYPE html>
<html lang="ja">
<head>
<meta charset="utf-8">
<title>株式会社キリノハコビヤ 路上看板</title>
<link rel="stylesheet" href="https://fonts.googleapis.com/css2?family=Shippori+Mincho:wght@500&family=M+PLUS+1p:wght@800;900&family=Cormorant+Garamond:wght@500&display=swap">
<style>
:root{
  --green:#1e6b3d;
  --green-deep:#17592f;
  --green-light:#3f8a55;
  --white:#ffffff;
  --photo-warm:#8a6a4e;
  --photo-wall:#4a3a30;
  --photo-light:#e8e2d8;
}
html,body{margin:0;padding:0;overflow:hidden;}
body{width:1200px;height:2223px;}
.signboard{
  position:relative;width:1200px;height:2223px;overflow:hidden;
  background:var(--green);color:var(--white);
}
.headline{
  position:absolute;top:118px;left:0;width:1200px;margin:0;
  font-family:"Shippori Mincho",serif;font-weight:500;
  font-size:72px;line-height:132px;letter-spacing:22px;text-align:center;
}
.interior-photo{
  position:absolute;left:72px;top:482px;width:1056px;height:490px;
  background:linear-gradient(180deg,var(--photo-wall) 0%,var(--photo-wall) 30%,var(--photo-light) 31%,#d9d2c6 60%,var(--photo-warm) 61%,#6e5037 100%);
}
.company{
  position:absolute;left:0;width:1200px;text-align:center;white-space:nowrap;
  font-family:"M PLUS 1p",sans-serif;
}
.company-type{top:1136px;font-size:84px;font-weight:800;letter-spacing:4px;line-height:1;}
.company-name{top:1240px;font-size:136px;font-weight:900;letter-spacing:8px;line-height:1;}
.phone{
  position:absolute;top:1422px;left:0;width:1200px;
  display:flex;flex-wrap:nowrap;justify-content:center;align-items:center;gap:16px;
  white-space:nowrap;
  font-family:"M PLUS 1p",sans-serif;font-weight:900;font-size:118px;letter-spacing:4px;line-height:1;
}
.phone-icon{width:92px;height:92px;flex:none;}
.lower-curves{position:absolute;left:0;top:1560px;width:1200px;height:663px;}
.brand{
  position:absolute;left:132px;top:1904px;width:936px;height:128px;
  box-sizing:border-box;border:3px solid var(--white);
  display:flex;align-items:center;justify-content:center;white-space:nowrap;
  font-family:"Cormorant Garamond",serif;font-weight:500;font-size:76px;letter-spacing:3px;
}
.brand-sub{
  position:absolute;top:2058px;left:0;width:1200px;text-align:center;
  font-family:"Cormorant Garamond",serif;font-weight:500;font-size:44px;letter-spacing:10px;
}
</style>
</head>
<body>
<div class="signboard">
  <p class="headline">デザイン住宅を<br>お値打ちで建てる。</p>
  <div class="interior-photo" role="img" aria-label="木目の床と白いソファのある明るいリビングの写真"></div>
  <div class="company company-type">株式会社</div>
  <div class="company company-name">キリノハコビヤ</div>
  <div class="phone">
    <svg class="phone-icon" viewBox="0 0 100 100" aria-hidden="true">
      <circle cx="50" cy="50" r="44" fill="none" stroke="#fff" stroke-width="8"/>
      <path d="M36 26c4 0 6 8 6 11s-5 4-5 6c0 5 9 15 14 15 2 0 3-5 6-5s11 2 11 6-5 10-10 10C42 69 31 52 31 39c0-6 1-13 5-13z" fill="#fff"/>
    </svg>
    <span>0574-83-5167</span>
  </div>
  <svg class="lower-curves" viewBox="0 0 1200 663" aria-hidden="true">
    <path d="M0 40 Q600 380 1200 40 L1200 663 L0 663Z" fill="var(--green-light)"/>
    <path d="M0 120 Q600 420 1200 120 L1200 663 L0 663Z" fill="var(--white)"/>
    <path d="M0 150 Q600 440 1200 150 L1200 663 L0 663Z" fill="var(--green-deep)"/>
  </svg>
  <div class="brand">KIRINO HAKOBIYA</div>
  <div class="brand-sub">MINO STUDIO</div>
</div>
</body>
</html>
```